I need an out door banner to help me promote my classes, i am a dating coach. i would like to see designs that use the colors. black, yellow, pink, white,orange. colors that attract women. the final design should communicate how women can Reclaim Every Spark, Shine Once More.

Target Market(s)

Bright Mornings After Midnight Storms: Reclaim Every Spark, Shine Once More: Heartfelt Wisdom on Modern Courtship

Industry/Entity Type

dating advice

Logo Text

Attention Ladies: Weed out the Narcissist, the abusers, the couch potatoes, the players & the losers...( Expose & Dump his #ss before he destroys your life)

Colors

Designer to choose colors to be used in the design.

Requirements
Nice to have
• Some bold text too
Should not have
• black round

```html
<!DOCTYPE html>
<html lang="en">
<head>
<meta charset="utf-8">
<title>Ladies Support Group Banner</title>
<link rel="stylesheet" href="https://fonts.googleapis.com/css2?family=Archivo:wdth,wght@125,800;125,900&family=Barlow+Condensed:wght@600;700;800&family=Barlow+Semi+Condensed:wght@700;800&family=Barlow:wght@800&display=swap">
<style>
  :root {
    --pink: #ff4ba6;
    --yellow: #fff500;
    --black: #0a0a0a;
    --white: #ffffff;
    --red: #ec1c1c;
    --grey: #333333;
  }
  html, body {
    margin: 0;
    padding: 0;
    width: 756px;
    height: 1200px;
    overflow: hidden;
  }
  .banner {
    position: relative;
    width: 756px;
    height: 1200px;
    background: var(--pink);
    overflow: hidden;
  }
  .callout {
    position: absolute;
    left: 53px;
    width: 649px;
    background: var(--white);
    border-radius: 8px;
    color: var(--black);
    text-align: center;
    font-family: "Barlow Semi Condensed", sans-serif;
    font-weight: 700;
  }
  .callout--top {
    top: 61px;
    height: 112px;
    font-size: 79px;
    line-height: 112px;
    letter-spacing: 0.5px;
  }
  .callout--warning {
    top: 879px;
    height: 119px;
    font-size: 46px;
    line-height: 48px;
    padding-top: 12px;
    box-sizing: border-box;
  }
  .headline {
    position: absolute;
    left: 0;
    top: 0;
    width: 756px;
    height: 1200px;
  }
  .wide { font-family: "Archivo", sans-serif; font-stretch: 125%; }
  .weed { fill: var(--white); font-weight: 800; }
  .out { fill: var(--black); font-weight: 900; }
  .cond { font-family: "Barlow Condensed", sans-serif; font-weight: 700; }
  .semi { font-family: "Barlow Semi Condensed", sans-serif; font-weight: 800; }
  .article { font-family: "Barlow", sans-serif; font-weight: 800; fill: var(--white); }
  .yellow { fill: var(--yellow); }
  .black { fill: var(--black); }
  .white { fill: var(--white); }

  .offer-band {
    position: absolute;
    left: 0;
    top: 1028px;
    width: 756px;
    height: 147px;
    background: var(--yellow);
  }
  .badge {
    position: absolute;
    top: 38px;
    width: 120px;
    height: 120px;
    border-radius: 50%;
    background: var(--pink);
    border: 7px solid var(--white);
    display: flex;
    flex-direction: column;
    align-items: center;
    justify-content: center;
    color: var(--black);
    font-family: "Barlow Condensed", sans-serif;
    font-weight: 700;
  }
  .badge--free { left: 19px; top: 9px; font-size: 56px; letter-spacing: -1px; }
  .badge--price { left: 603px; top: 9px; }
  .badge__reg { color: var(--grey); font-family: "Barlow Semi Condensed", sans-serif; font-size: 28px; line-height: 26px; }
  .badge__amount { font-size: 56px; line-height: 50px; }
  .offer-details {
    position: absolute;
    left: 163px;
    top: 20px;
    width: 433px;
    text-align: center;
  }
  .offer-details__title {
    font-family: "Archivo", sans-serif;
    font-stretch: 125%;
    font-weight: 800;
    font-size: 25px;
    letter-spacing: 1.5px;
    line-height: 30px;
    color: var(--black);
  }
  .offer-details__schedule {
    font-family: "Barlow Semi Condensed", sans-serif;
    font-weight: 700;
    font-size: 36px;
    line-height: 42px;
    color: var(--red);
  }
  .offer-details__address {
    font-family: "Barlow Semi Condensed", sans-serif;
    font-weight: 700;
    font-size: 20px;
    line-height: 26px;
    color: var(--black);
  }
</style>
</head>
<body>
<main class="banner">
  <div class="callout callout--top">Attention Ladies!</div>

  <svg class="headline" viewBox="0 0 756 1200" xmlns="http://www.w3.org/2000/svg" aria-label="Weed out the narcissist, the abusers, the couch potatoes, the players and the losers">
    <text class="wide weed" x="63" y="282" font-size="108" textLength="335" lengthAdjust="spacingAndGlyphs">Weed</text>
    <text class="wide out" x="430" y="282" font-size="108" textLength="266" lengthAdjust="spacingAndGlyphs">OUT</text>

    <text class="article" transform="translate(112 354) rotate(-90)" text-anchor="middle" font-size="62" textLength="88" lengthAdjust="spacingAndGlyphs">the</text>
    <text class="cond yellow" x="125" y="398" font-size="124" textLength="572" lengthAdjust="spacingAndGlyphs">NARCISSIST</text>

    <text class="article" x="63" y="466" font-size="62" textLength="93" lengthAdjust="spacingAndGlyphs">the</text>
    <text class="semi black" x="158" y="524" font-size="140" textLength="539" lengthAdjust="spacingAndGlyphs">ABUSERS</text>

    <text class="article" transform="translate(104 588) rotate(-90)" text-anchor="middle" font-size="55" textLength="76" lengthAdjust="spacingAndGlyphs">the</text>
    <text class="cond yellow" x="116" y="626" font-size="108" textLength="581" lengthAdjust="spacingAndGlyphs">COUCH POTATOES</text>

    <text class="article" x="63" y="690" font-size="62" textLength="94" lengthAdjust="spacingAndGlyphs">the</text>
    <text class="semi black" x="168" y="735" font-size="122" textLength="444" lengthAdjust="spacingAndGlyphs">PLAYERS</text>
    <text class="semi white" x="623" y="735" font-size="122" textLength="74" lengthAdjust="spacingAndGlyphs">&amp;</text>

    <text class="article" transform="translate(174 800) rotate(-90)" text-anchor="middle" font-size="62" textLength="84" lengthAdjust="spacingAndGlyphs">the</text>
    <text class="semi yellow" x="190" y="842" font-size="118" textLength="451" lengthAdjust="spacingAndGlyphs">LOSERS...</text>
  </svg>

  <div class="callout callout--warning">Expose &amp; Dump his *ss<br>before he destroys your life</div>

  <section class="offer-band">
    <div class="badge badge--free">FREE</div>
    <div class="offer-details">
      <div class="offer-details__title">LADIES SUPPORT GROUP</div>
      <div class="offer-details__schedule">Classes Every Wed @ 12 am</div>
      <div class="offer-details__address">4820 Linden Ave No appt. Walk-ins ecceppted</div>
    </div>
    <div class="badge badge--price">
      <span class="badge__reg">Reg</span>
      <span class="badge__amount">$97</span>
    </div>
  </section>
</main>
</body>
</html>
```